New eyelid plastic surgery office needs a business card design-Eyelid Surgery Partners of Brennor

I recently used SketchHarbor for my logo design and was very pleased with creativity and results. It was a difficult decision for me. Now I would like to create a business card based on this logo, which I will attach.

The text should be easily legible as some of my patients have difficulty seeing, but I would like a subtle, sophisticated artistry also evident to make the card memorable. Would like the card based on a similar color scheme as the logo but the inverse or other complementary colors may prove interesting

A good question was asked...my concern about my visually impaired patients was really my desire to avoid italicized or calligraphic type fonts that may be hard to read. Standard font size for a business card would be fine. Thanks!

Thank you so much for the great work so far. I wanted to give you my particular contact information to see if that would change the look of the cards. Martin Pellowby, MD Address: 2817 Larkmoor Avenue, Suite 205 Wilmington, NC 28517 Phone: 910-555-0183 Fax: 910-555-0184 Website: www.brennorlidclinic.example Please delete the email slot from the card. Thanks so much!

Reason: Last minute consideration. So many great revisions right now!

Plastic

```html
<!DOCTYPE html>
<html lang="en">
<head>
<meta charset="utf-8">
<title>Eyelid Surgery Partners of Brennor – Business Card</title>
<link rel="stylesheet" href="https://fonts.googleapis.com/css2?family=Source+Sans+3:wght@400;600&display=swap">
<style>
  :root {
    --backdrop: #e6e6ea;
    --card: #ffffff;
    --brand-blue: #0b58a8;
    --text-blue: #0d4f9c;
    --band-gray: #c9cacd;
    --shadow: rgba(40, 40, 60, 0.28);
  }
  * { box-sizing: border-box; margin: 0; padding: 0; }
  html, body {
    width: 1200px;
    height: 900px;
    overflow: hidden;
    background: var(--backdrop);
    font-family: "Source Sans 3", "Helvetica Neue", Arial, sans-serif;
    color: var(--text-blue);
  }
  .card-set {
    position: absolute;
    left: 50px;
    top: 301px;
    display: flex;
    gap: 60px;
  }
  .card {
    position: relative;
    width: 520px;
    height: 298px;
    background: var(--card);
    box-shadow: 4px 6px 14px var(--shadow);
    overflow: hidden;
  }
  .card-swoosh {
    position: absolute;
    inset: 0;
    width: 100%;
    height: 100%;
  }
  .swoosh-band { fill: var(--band-gray); }
  .swoosh-accent { fill: var(--brand-blue); }

  /* Front */
  .brand-name {
    position: absolute;
    left: 0;
    right: 0;
    top: 104px;
    text-align: center;
    font-weight: 400;
    color: var(--text-blue);
    text-transform: uppercase;
    line-height: 1.05;
  }
  .brand-name .line-main {
    display: block;
    font-size: 33px;
    letter-spacing: 0.5px;
  }
  .brand-name .line-sub {
    display: block;
    font-size: 19px;
    letter-spacing: 1.5px;
    margin-top: 4px;
  }

  /* Back */
  .appointment {
    position: absolute;
    left: 25px;
    top: 22px;
  }
  .appointment-title {
    font-size: 22px;
    font-weight: 600;
    line-height: 1.1;
  }
  .appointment-hours {
    font-size: 16px;
    font-weight: 400;
    line-height: 1.4;
    margin-top: 3px;
  }
  .contact {
    position: absolute;
    right: 40px;
    top: 112px;
    text-align: right;
    font-style: normal;
    font-size: 18px;
    line-height: 1.3;
  }
  .contact-phone {
    font-size: 22px;
    font-weight: 600;
    margin-bottom: 10px;
  }
  .contact-web { line-height: 1.1; }
</style>
</head>
<body>
  <main class="card-set">
    <section class="card card-front" aria-label="Card front">
      <svg class="card-swoosh" viewBox="0 0 340 195" preserveAspectRatio="none" aria-hidden="true">
        <path class="swoosh-band" d="M0,146 C110,172 280,152 340,62 L340,195 L0,195 Z"/>
        <path class="swoosh-accent" d="M340,84 C322,150 262,184 208,195 L340,195 Z"/>
      </svg>
      <h1 class="brand-name">
        <span class="line-main">Eyelid Surgery Partners</span>
        <span class="line-sub">of Brennor</span>
      </h1>
    </section>

    <section class="card card-back" aria-label="Card back">
      <svg class="card-swoosh" viewBox="0 0 340 195" preserveAspectRatio="none" aria-hidden="true">
        <path class="swoosh-band" d="M0,68 C28,150 180,186 340,166 L340,195 L0,195 Z"/>
        <path class="swoosh-accent" d="M0,86 C14,140 70,180 136,195 L0,195 Z"/>
      </svg>
      <div class="appointment">
        <h2 class="appointment-title">Appointment</h2>
        <p class="appointment-hours">Mon - Fri 08 a.m - 08 p.m.<br>Sat 08 a.m - 01 p.m.</p>
      </div>
      <address class="contact">
        <p class="contact-phone">000 000 000</p>
        <p class="contact-address">Build, Street,<br>0000 00 City</p>
        <p class="contact-web">email@site.example<br>www.site.example</p>
      </address>
    </section>
  </main>
</body>
</html>
```